New Website design 2024: Ridgeline Flameguard, Inc.

1. Who we are: At Ridgeline Flameguard Inc, our mission is to provide our clients with comprehensive firestop and seismic expansion joint solutions that ensure the safety and integrity of their buildings. We specialize in the installation of firestop systems at penetrations, wall joints, and slab edge joints, as well as providing acoustical sealants, security sealants, architectural caulking, and seismic expansion joints. Since our establishment in 2007, we have been committed to improving the safety and integrity of buildings through our expertise and use of tested and approved firestop systems. Our focus is to deliver exceptional service and quality workmanship to ensure the protection of lives and property.
2. Services we provide:
-Firestopping: T-ratings, CMU Wall Joint, Exterior Caulking, Fireproof Patching, Head of Wall Joints, Through Penetrations, Curtain Wall/Slab Edge, Grease & Fume Duct Protection.
-Expansion Joints: Floor Covers, Roof Covers, Fire Barriers, Vapor Barriers, Wall & Ceiling Covers, Compression Seals, Pre-Compression Foams, Photoluminescent Signage
3. Examples of scope and projects we’ve completed.
4. How to contact us.: https://ridgelineflameguard.example/contact/
- Social Media Links: https://www.linkedin.example/company/ridgeline-flameguard/mycompany/
https://www.instagram.example/ridgelineflameguard/?hl=en
https://www.youtube.example/channel/UCQ8M2RT5KwpZdNvTeLoJbHs/videos
Target Market(s)
Commercial Construction industry
Industry/Entity Type
Commercial Construction industry in California
Coding
Coded - Design and coding required
Number of Pages Required
4 page
Colors
Designer to choose colors to be used in the design.
Requirements
Must have
- 1. Who we are. 2. Services we provide. 3. Examples of scope and projects we’ve completed. 4. How to contact us.
Nice to have
- Logo. Pictures of scope of work and pictures of projects completed or working on.
Should not have
- Names of clients.

```html
<!DOCTYPE html>
<html lang="en">
<head>
<meta charset="utf-8">
<title>Contact – Ridgeline Flameguard, Inc.</title>
<link href="https://fonts.googleapis.com/css2?family=Inter:wght@400;500;600;700&family=Krona+One&display=swap" rel="stylesheet">
<style>
:root{
  --ink:#141414;
  --bar:#121212;
  --footer:#181818;
  --red:#e3261f;
  --blue:#1a5c9c;
  --field:#f0f0f0;
  --field-line:#8a8a8a;
  --white:#ffffff;
  --muted:#3a3a3a;
}
*{box-sizing:border-box;margin:0;padding:0}
html,body{width:684px;height:1200px;overflow:hidden}
body{position:relative;background:var(--white);font-family:"Inter",sans-serif;color:var(--ink)}
.abs{position:absolute}
.display{font-family:"Krona One",sans-serif;text-transform:uppercase}

.topbar{left:0;top:0;width:684px;height:33px;background:var(--bar);color:var(--white);font-size:7.5px}
.topbar .contacts{left:71px;top:12px;display:flex;gap:9px}
.social{display:flex;gap:7px}
.social span{width:14px;height:14px;border:1px solid currentColor;border-radius:50%;display:block}
.topbar .social{right:71px;top:9px;color:var(--white)}

.nav{left:0;top:33px;width:684px;height:46px;background:var(--white)}
.brand{display:flex;align-items:center;gap:5px;font-weight:700;font-size:11px;color:var(--red);letter-spacing:.2px}
.brand i{width:9px;height:9px;background:var(--red);display:block}
.nav .brand{left:71px;top:16px}
.menu{left:265px;top:19px;display:flex;gap:15px;font-size:7.5px;font-weight:500}
.cta{display:block}
.nav .cta{left:484px;top:10px}
.cta-label{position:absolute;color:var(--white);font-weight:600;font-size:7.5px}

.hero{left:0;top:79px;width:684px;height:218px;background:linear-gradient(120deg,#2b2b2b 0%,#3e3d3b 40%,#1f1f1f 70%,#2d2c2a 100%)}
.hero-kicker{left:0;top:162px;width:684px;display:flex;justify-content:center;align-items:center;gap:28px;color:var(--white);font-size:12px;font-weight:600;letter-spacing:2px}
.hero-kicker b{width:95px;height:1px;background:rgba(255,255,255,.7);display:block}
.hero-title{left:0;top:186px;width:684px;text-align:center;color:var(--white);font-size:19.5px;line-height:25px}

.eyebrow{left:0;top:351px;width:684px;text-align:center;color:var(--red);font-weight:600;font-size:12px;letter-spacing:2px}
.section-title{left:0;top:373px;width:684px;text-align:center;font-size:17.5px}
.intro{left:142px;top:410px;width:400px;text-align:center;font-size:7px;line-height:13px;color:var(--muted)}

.card{top:482px;width:173px;height:92px;border:1px solid var(--blue);text-align:center}
.card h3{font-family:"Krona One",sans-serif;font-size:10.5px;margin-top:40px}
.card h3.tall{margin-top:35px}
.card p{font-size:7px;line-height:11px;margin-top:6px;color:var(--muted)}
.badge{top:-22px;left:66px;width:40px;height:40px;border-radius:50%;background:var(--red);display:flex;align-items:center;justify-content:center}

.form-title{left:0;top:613px;width:684px;text-align:center;font-size:9px}
.field{left:164px;width:357px;background:var(--field);border:1px solid var(--field-line);font-size:7.5px;text-align:center;padding-top:12px;color:var(--ink)}
.send{left:278px;top:882px}

.footer{left:0;top:966px;width:684px;height:234px;background:var(--footer);color:var(--white)}
.footer .brand{left:0;width:684px;top:48px;justify-content:center}
.footer .about{left:142px;top:86px;width:400px;text-align:center;font-size:7px;line-height:13px}
.footer .social{left:0;width:684px;top:131px;justify-content:center;gap:10px}
.footer .social span{width:17px;height:17px}
.footer .rule{left:71px;top:192px;width:542px;height:1px;background:rgba(255,255,255,.55)}
.footer .copy{left:0;top:210px;width:684px;text-align:center;font-size:7px}
</style>
</head>
<body>

<header class="abs topbar">
  <div class="abs contacts"><span>123-456-789</span><span>|</span><span>info@ridgeline.example</span></div>
  <div class="abs social"><span></span><span></span><span></span></div>
</header>

<nav class="abs nav">
  <div class="abs brand"><i></i>Ridgeline Flameguard</div>
  <div class="abs menu"><span>Who We Are</span><span>Our Services</span><span>Our Projects</span></div>
  <div class="abs cta">
    <svg width="129" height="26" viewBox="0 0 129 26">
      <rect x="0" y="0" width="105" height="24" fill="#1a5c9c"/>
      <polygon points="95,0 129,0 129,26 103,26" fill="#e3261f"/>
      <circle cx="115" cy="12.5" r="4.5" fill="none" stroke="#fff" stroke-width="1.5"/>
      <circle cx="115" cy="12.5" r="1.5" fill="#fff"/>
    </svg>
    <span class="cta-label" style="left:27px;top:8px">Contact Us</span>
  </div>
</nav>

<section class="abs hero" role="img" aria-label="Photo of hands using a tablet beside a laptop and coffee cup"></section>
<div class="abs hero-kicker"><b></b>Contact Us<b></b></div>
<h1 class="abs hero-title display">Lorem Ipsum is a<br>dummy text</h1>

<div class="abs eyebrow">Contact</div>
<h2 class="abs section-title display">Get in touch with us</h2>
<p class="abs intro">Lorem Ipsum is simply dummy text of the printing and typesetting industry. Lorem Ipsum has been the industry's standard dummy text ever since the 1500s,</p>

<div class="abs card" style="left:71px">
  <div class="abs badge"><svg width="16" height="16" viewBox="0 0 24 24"><path d="M6.6 10.8a15 15 0 0 0 6.6 6.6l2.2-2.2c.3-.3.7-.4 1-.2 1.1.4 2.3.6 3.6.6.6 0 1 .4 1 1V20c0 .6-.4 1-1 1A17 17 0 0 1 3 4c0-.6.4-1 1-1h3.5c.6 0 1 .4 1 1 0 1.3.2 2.5.6 3.6.1.3 0 .7-.2 1z" fill="#fff"/></svg></div>
  <h3>Call Now!</h3>
  <p>123-456-7890</p>
</div>
<div class="abs card" style="left:256px">
  <div class="abs badge"><svg width="14" height="16" viewBox="0 0 24 28"><path d="M12 1a9 9 0 0 0-9 9c0 7 9 17 9 17s9-10 9-17a9 9 0 0 0-9-9zm0 12.5a3.5 3.5 0 1 1 0-7 3.5 3.5 0 0 1 0 7z" fill="#fff"/></svg></div>
  <h3 class="tall">Address</h3>
  <p>Lorem Ipsum is simply dummy text of<br>the printing and typesetting industry.</p>
</div>
<div class="abs card" style="left:441px">
  <div class="abs badge"><svg width="18" height="14" viewBox="0 0 24 18"><rect x="1" y="1" width="22" height="16" fill="#fff"/><path d="M1 1l11 9 11-9" fill="none" stroke="#e3261f" stroke-width="1.5"/></svg></div>
  <h3>Email Now!</h3>
  <p>info@ridgeline.example</p>
</div>

<h2 class="abs form-title display">Or you can message us</h2>
<div class="abs field" style="top:643px;height:35px">Name</div>
<div class="abs field" style="top:685px;height:35px">Email</div>
<div class="abs field" style="top:728px;height:134px">Message</div>
<div class="abs send">
  <svg width="129" height="26" viewBox="0 0 129 26">
    <rect x="0" y="0" width="105" height="24" fill="#1a5c9c"/>
    <polygon points="97,0 129,0 129,26 105,26" fill="#e3261f"/>
    <path d="M111 13l12-6-4 13-3-4-3 2z" fill="#fff"/>
  </svg>
  <span class="cta-label" style="left:39px;top:8px">Send</span>
</div>

<footer class="abs footer">
  <div class="abs brand"><i></i>Ridgeline Flameguard</div>
  <p class="abs about">Lorem Ipsum is simply dummy text of the printing and typesetting industry. Lorem Ipsum has been the industry's standard dummy text ever since the 1500s,</p>
  <div class="abs social"><span></span><span></span><span></span></div>
  <div class="abs rule"></div>
  <div class="abs copy">Copyright@2023-Ridgeline Flameguard-Privacy Policy</div>
</footer>

</body>
</html>
```